Gestaltung eines Merkblattes
Ein Entwurf, der genau meinen Vorstellungen entspricht. Eine Abwicklung, die schneller und professioneller nicht sein könnte. Die Kommunikation - sehr symphatisch und kundenorientiert. Resumee: Besser geht es nicht.
Zielgruppe
www.hufspur-praxis.de/ Medizinische Bioresonanzanalysen für Pferde. Die Kundschaft besteht hauptsächlich aus Frauen, Alter von 20- 55 Jahre.
Bei dem Projekt handelt es sich um die Gestaltung eines wichtigen Merkblattes, das jedem Kunde zusammen mit dem Befund der Analyse gemailt wird. Es enthält wichtige Informationen rund um die Bioresonanzanalyse und sollte als pdf- Datei vorliegen.
Aufgabenstellung
Kernproblem: Die Kunden lesen das Merkblatt gar nicht oder nicht sorgfältig. So entstehen viele Fragen in der Folge, die nicht notwendig wären.
Wir benötigen eine pdf- Datei, die zum Lesen anregt, gerne gelesen wird und in der die wichtigsten Aspekte in das Auge fallen. Diese wurden von mir in der Worddatei, die den Text enthält, rot markiert.
Der Text in schwarz ist deutlich weniger wichtig.
Ach ja, die Überschrift ist doof. 'Allgemeine Hinweise' das animiert nicht wirklich zum Lesen. Falls Sie eine griffige Idee haben, sehr gerne.

```html
<!DOCTYPE html>
<html lang="de">
<head>
<meta charset="utf-8">
<title>Merkblatt – Hinweise zur Bioresonanzanalyse</title>
<link rel="stylesheet" href="https://fonts.googleapis.com/css2?family=Roboto:wght@400;500&display=swap">
<style>
  :root {
    --paper: #ffffff;
    --ink: #1b1b1b;
    --heading: #111111;
    --frame: #4a4a4a;
  }
  * { box-sizing: border-box; margin: 0; padding: 0; }
  html, body {
    width: 848px;
    height: 1200px;
    overflow: hidden;
    background: var(--paper);
  }
  .sheet {
    position: relative;
    width: 848px;
    height: 1200px;
    border: 1px solid var(--frame);
    padding: 46px 55px 0 61px;
    font-family: "Roboto", Arial, sans-serif;
    color: var(--ink);
    font-size: 14.6px;
    line-height: 22.6px;
    white-space: nowrap;
  }
  .section-title {
    font-size: 24px;
    font-weight: 500;
    line-height: 30px;
    color: var(--heading);
    margin: 14px 0 7px;
  }
  .section-title:first-child { margin-top: 0; }
  .section-title.minor {
    font-size: 20.5px;
    margin-top: 16px;
  }
  .note + .note { margin-top: 22.6px; }
</style>
</head>
<body>
<main class="sheet">

  <section class="topic">
    <h2 class="section-title">Tierarzt</h2>
    <p class="note">Wir weisen ausdrücklich darauf hin, dass die Ergebnisse der Bioresonanzanalyse nicht kompa-<br>tibel sind mit den herkömmlichen Labormethoden und anderen tierärztlichen Diagnoseformen.</p>
    <p class="note">Ein Beispiel: Wenn wir eine Belastung der Leber mit dem Leberegel Fasciola hepatica feststel-<br>len, kann eine klassische Laboruntersuchung&nbsp; zu dem gleichen Thema ergebnislos bleiben. Der<br>Grund hierfür liegt u.a. in der sehr unterschiedlichen Beurteilung und Herangehensweise.</p>
    <p class="note">Das Wohl Ihres Pferdes steht jederzeit im Mittelpunkt. Falls in der Zeit der Umsetzung der The-<br>rapie-empfehlung bei Ihrem Pferd Symptome auftreten, die eine tierärztliche und schnelle Hilfe<br>dringend erforderlich machen, zögern Sie bitte nie, den Tierarzt zu rufen.</p>
    <p class="note">Bitte informieren Sie mich vorab, wenn Ihr Pferd zum Zeitpunkt der Nachtestung Medikamente<br>von dem Tierarzt erhält. Relevant sind Antibiotika, Cortison, sowie andere, massiv&nbsp; entzün-<br>dungshemmende Präparate.&nbsp; In diesem Fall sprechen wir miteinander ab, ob die Nachtestung<br>verschoben wird. Wurmkuren und Impfungen sind für die Durchführung der Nachtestung nicht<br>von Bedeutung.</p>
  </section>

  <section class="topic">
    <h2 class="section-title">Impfung</h2>
    <p class="note">Wir geben generell keine Impfempfehlungen. Es hat sich jedoch in den vergangenen Jahren<br>gezeigt, dass es sinnvoll ist, Impfungen (besonders Influenza- und Herpes- Impfungen) vor<br>Beginn der Umsetzung der Therapieempfehlung einzuplanen. Werden sie zu einem späteren<br>Zeitpunkt&nbsp; vorgenommen, kann es zu Rückschritten in der ansonsten positiven Entwicklung<br>kommen.</p>
  </section>

  <section class="topic">
    <h2 class="section-title">Doping</h2>
    <p class="note">Zum Schutz der Pferde bestehen Anti-Doping Richtlinien, die klare Regeln vorgeben, welche<br>Zu- satzfutterpräparate, Medikamente und auch Naturheilmittel einem Turnierpferd vor und<br>während einem Start in einer Turnierprüfung gefüttert werden dürfen. Die Einhaltung der Vor-<br>gaben wird durch stichpunktartige Kontrollen überprüft.</p>
    <p class="note">Bitte beachten Sie die Anti- Doping Richtlinien der RVD und weiterer Pferdesportverbände und<br>halten Sie bei der Fütterung aller Präparate unserer Therapieempfehlung eine Karenzzeit von<br>48 Stunden vor Prüfungsbeginn ein, wenn Sie mit Ihrem Pferd an einem Wettbewerb teilneh-<br>men. Ausnahme! Bei der Zufütterung von Präparaten, die Teufelskralle enthalten, besteht eine<br>Karenzzeit von 4 Tagen.</p>
    <p class="note">Wir übernehmen für die Folgen einer Nichtbeachtung der nationalen oder internationalen Anti-<br>Dopingrichtlinien keine Haftung.</p>
  </section>

  <section class="topic">
    <h2 class="section-title minor">Tragende Stuten/ Stuten mit Fohlen bei Fuß</h2>
    <p class="note">Wir übernehmen keine Haftung für die Gabe der von uns empfohlenen Naturheilmittel bei tra-<br>genden Stute und Stuten mit Fohlen bei Fuß. Jedes der angegebenen Mittel wurde von mir mit<br>großer Sorgfalt ausgewählt. Die aktuell vorhandenen, medizinischen Studien zu der Wirkung<br>von Naturheilmitteln bei tragenden Stuten sind jedoch nicht umfangreich genug, um Nebenwir-<br>kungen vollständig ausschließen zu können.</p>
  </section>

</main>
</body>
</html>
```